Shoes & Inserts Postcard Campaign

Hi,
We are looking to send a postcard to our patients reminding them that they may be eligible for shoes and inserts in the new calendar year. The patient demographic is mostly 50 and above.

We plan on uploading the image to Kolbo Press and have them create the postcard for us to be sent out.
Dimensions: 4.2"x5.5"
Front & Back Design
Images should be in high resolution. Entire postcard to be high resolution, if not vector.
I've attached a sample of what we used to have with the dimension parameters and our logo.

Verbiage can be the same, switch it to 2023. Front of the postcard doesn't need our logo. Looking for eye catching. Warm and welcoming.

Thank you,
Tomas Ibe

```html
<!DOCTYPE html>
<html lang="en">
<head>
<meta charset="utf-8">
<title>Shoes &amp; Inserts Postcard</title>
<link rel="stylesheet" href="https://fonts.googleapis.com/css2?family=Poppins:wght@300;400;500;600&family=Oswald:wght@400&family=Arvo:wght@700&family=Nunito:wght@800;900&display=swap">
<style>
  :root{
    --navy:#253a4c;
    --peach-title:#f6b89f;
    --coral:#f58f86;
    --coral-deep:#f27464;
    --sand:#f8bfae;
    --panel:#f9d3c1;
    --orange:#f5884a;
    --ink:#1c1c1c;
    --grey:#555b60;
    --rule:#9a9a9a;
    --stamp:#221f20;
    --white:#ffffff;
  }
  *{margin:0;padding:0;box-sizing:border-box}
  html,body{width:862px;height:1200px;overflow:hidden;background:var(--navy)}
  .canvas{position:relative;width:862px;height:1200px;background:var(--navy);font-family:'Poppins',sans-serif}
  .sheet-title{position:absolute;top:74px;left:0;width:100%;text-align:center;color:var(--peach-title);font-weight:600;font-size:30px;letter-spacing:5px}

  .card{position:absolute;left:134px;width:595px;height:461px;overflow:hidden}
  .card-front{top:152px;background:var(--coral)}
  .card-back{top:661px;background:var(--white)}

  .front-art{position:absolute;inset:0}
  .shoe-photo{position:absolute;left:194px;top:76px;width:206px;height:284px;border-radius:90px 60px 40px 40px;background:linear-gradient(160deg,#f2e8dc 0%,#d9b99a 55%,#f1ede6 100%)}
  .offer-panel{position:absolute;left:353px;top:73px;width:211px;height:178px;background:var(--panel);border-top-right-radius:70px}
  .offer-kicker{position:absolute;left:369px;top:110px;font-family:'Oswald',sans-serif;font-size:14px;color:var(--coral-deep);letter-spacing:.2px;white-space:nowrap}
  .offer-headline{position:absolute;left:367px;top:134px;font-family:'Arvo',serif;font-weight:700;font-size:39px;line-height:37px;color:var(--white);text-shadow:0 2px 6px rgba(230,120,100,.35)}

  .contact{position:absolute;top:398px;white-space:nowrap}
  .contact-call{left:15px}
  .contact-visit{left:403px}
  .contact-label{font-weight:300;font-size:18px;color:#3d3533;line-height:22px}
  .contact-value{font-family:'Nunito',sans-serif;font-weight:900;font-size:22px;color:var(--coral-deep);line-height:26px;letter-spacing:.5px}

  .practice-name{position:absolute;left:23px;top:23px;display:flex;align-items:center;gap:8px;height:48px}
  .practice-mark{width:14px;height:14px;background:#5ec3a6}
  .practice-text{font-weight:600;font-size:15px;color:var(--orange);line-height:18px}
  .tagline{position:absolute;left:210px;top:33px;font-weight:600;font-size:18.2px;color:var(--orange);white-space:nowrap}
  .practice-address{position:absolute;left:23px;top:78px;font-size:10.5px;line-height:13.5px;color:var(--grey)}
  .stamp-box{position:absolute;left:460px;top:25px;width:107px;height:107px;background:var(--stamp);color:var(--white);display:flex;align-items:center;justify-content:center;text-align:center;font-size:14px;line-height:17px}
  .notice{position:absolute;left:23px;top:129px;font-weight:600;font-size:17.2px;line-height:22.3px;color:var(--ink)}
  .notice .accent{color:var(--coral-deep);font-weight:500}
  .cta{position:absolute;left:23px;top:246px;font-size:15.8px;line-height:20px;color:var(--grey)}
  .fine-print{position:absolute;left:23px;top:318px;font-size:10.5px;line-height:15px;color:var(--grey)}
  .fine-print p{margin-bottom:3px}
  .fine-print .date{color:var(--orange);font-weight:500}
  .fine-print .indent{padding-left:15px}
  .address-lines{position:absolute;left:323px;top:218px;width:244px}
  .address-lines span{display:block;height:1px;background:var(--rule);margin-bottom:21.7px}
</style>
</head>
<body>
<div class="canvas">
  <h1 class="sheet-title">POST CARD -MOCKUP 1</h1>

  <section class="card card-front">
    <svg class="front-art" width="595" height="461" viewBox="0 0 595 461">
      <g stroke="#ffffff" stroke-linecap="round" fill="none">
        <line x1="50" y1="42" x2="170" y2="-20" stroke-width="7" stroke-opacity=".35"/>
        <line x1="-20" y1="90" x2="200" y2="-20" stroke-width="22" stroke-opacity=".18"/>
        <line x1="-20" y1="130" x2="260" y2="-20" stroke-width="10" stroke-opacity=".2"/>
        <line x1="110" y1="145" x2="440" y2="-30" stroke-width="8" stroke-opacity=".25"/>
        <line x1="-10" y1="225" x2="430" y2="-20" stroke-width="6" stroke-opacity=".2"/>
        <line x1="90" y1="255" x2="440" y2="60" stroke-width="12" stroke-opacity=".18"/>
        <line x1="490" y1="80" x2="620" y2="-10" stroke-width="22" stroke-opacity=".2"/>
        <line x1="460" y1="60" x2="600" y2="-20" stroke-width="6" stroke-opacity=".25"/>
      </g>
      <polygon points="0,296 595,249 595,461 0,461" fill="#f8bfae"/>
    </svg>
    <div class="shoe-photo" role="img" aria-label="Photo of a pair of white and tan leather sneakers with orange heel tabs"></div>
    <div class="offer-panel"></div>
    <p class="offer-kicker">HAVE YOU ORDERED THIS YEARS</p>
    <h2 class="offer-headline">SHOES &amp;<br>INSERTS?</h2>
    <div class="contact contact-call">
      <p class="contact-label">Call Us</p>
      <p class="contact-value">(877) 555-0142</p>
    </div>
    <div class="contact contact-visit">
      <p class="contact-label">Visit Us</p>
      <p class="contact-value">newstride.com</p>
    </div>
  </section>

  <section class="card card-back">
    <div class="practice-name">
      <span class="practice-mark"></span>
      <span class="practice-text">Linden Foot &amp; Ankle</span>
    </div>
    <p class="tagline">We Keep You Moving</p>
    <p class="practice-address">88 Alder Park Road, Suite 210<br>Ashford, MD 21000</p>
    <div class="stamp-box">Postage<br>Stamp</div>
    <p class="notice">We are pleased to inform<br>that you may be eligible<br>for a <span class="accent">NEW</span> pair of shoes<br>and inserts!</p>
    <p class="cta">Please call our office<br>to schedule your appointment.</p>
    <div class="fine-print">
      <p>* Last day to place a shoe order is <span class="date">10/01/23.</span></p>
      <p>** if you have received your shoes and<br><span class="indent">inserts for 2023, please disregard.</span></p>
    </div>
    <div class="address-lines"><span></span><span></span><span></span><span></span></div>
  </section>
</div>
</body>
</html>
```